Staff Newsletter Template Image

We are looking for two .jpg images that we can put into a Word document and use for our staff newsletter. We will then add content using text boxes.
Attached is the current template which works for the columns and size that we need but we just want a fresh new design.
The Word document shows how we use it.
The name will stay the same - Team upBeat but can be a different look to the current one.

Target Market(s)

Sales team

Colors

Designer to choose colors to be used in the design.

Requirements
Must have
• Colours will be green, grey and white, possibly cream if needed. All from the guidelines.
• I have attached our brand guidelines which shows design elements and fonts for our brand. Also attached is brand guidelines for one of our product lines as we would like to use the same green.
• It needs to be nice to look at and motivational for our team

```html
<!DOCTYPE html>
<html lang="en">
<head>
<meta charset="utf-8">
<title>Team upBeat – Staff Newsletter</title>
<link rel="stylesheet" href="https://fonts.googleapis.com/css2?family=Jost:wght@300;400;500;600;700&display=swap">
<style>
  :root {
    --green: #7db733;
    --green-bright: #8cc63f;
    --green-deep: #447510;
    --heading-green: #82bc3c;
    --panel: #4b484a;
    --panel-dark: #3d3b3d;
    --line: #6c696b;
    --ink: #2b2a2c;
    --white: #ffffff;
    --muted: #b9b6b8;
  }
  * { box-sizing: border-box; margin: 0; padding: 0; }
  html, body { width: 848px; height: 1200px; overflow: hidden; background: var(--white); }
  body { font-family: "Jost", sans-serif; color: var(--ink); }
  .newsletter { position: relative; width: 848px; height: 1200px; overflow: hidden; background: var(--white); }
  .backdrop { position: absolute; inset: 0; }
  .masthead-name {
    position: absolute; left: 28px; top: 44px;
    font-size: 74px; font-weight: 400; letter-spacing: 1px; color: var(--ink); line-height: 1;
  }
  .issue-date {
    position: absolute; left: 625px; top: 178px;
    font-size: 36px; font-weight: 300; color: var(--white); line-height: 1;
  }
  .greeting {
    position: absolute; left: 35px; top: 314px;
    font-size: 25px; font-weight: 300; color: var(--ink);
  }
  .sidebar {
    position: absolute; left: 424px; top: 256px; width: 424px; height: 905px;
    background: var(--panel); color: var(--white);
  }
  .section-title {
    position: absolute; font-size: 20px; font-weight: 600; color: var(--heading-green); line-height: 1;
  }
  .intro {
    position: absolute; left: 62px; top: 105px; width: 300px;
    font-size: 11.5px; font-weight: 300; line-height: 17px;
  }
  .intro strong { font-weight: 600; }
  .sellers-table {
    position: absolute; left: 62px; top: 165px; width: 299px;
    border-collapse: collapse; font-size: 11.5px; font-weight: 300;
  }
  .sellers-table th, .sellers-table td {
    height: 34px; border: 1px solid var(--line); background: var(--panel-dark); vertical-align: middle;
  }
  .sellers-table th { font-weight: 600; background: var(--panel); }
  .sellers-table .rank { width: 32px; text-align: center; }
  .sellers-table .member { text-align: left; padding-left: 50px; }
  .tip-list { position: absolute; left: 75px; top: 419px; width: 300px; list-style: none; }
  .tip-list li {
    position: relative; padding-left: 14px; height: 49.6px;
    font-size: 11.5px; font-weight: 300; line-height: 17.5px;
  }
  .tip-list svg { position: absolute; left: -1px; top: 4px; width: 10px; height: 10px; }
  .field {
    position: absolute; left: 56px; width: 305px;
    border: 1px solid var(--line); background: var(--panel-dark);
    padding: 10px 22px; font-size: 11.5px; font-weight: 300; color: var(--muted);
  }
  .field-name { top: 706px; height: 35px; }
  .field-comments { top: 753px; height: 71px; }
  .submit-button {
    position: absolute; left: 56px; top: 841px; width: 102px; height: 34px;
    background: var(--green-bright); border-radius: 2px;
    color: var(--white); font-size: 13px; font-weight: 700; letter-spacing: 0.5px;
    display: flex; align-items: center; justify-content: center;
  }
  .footer-text {
    position: absolute; top: 1170px; font-size: 16px; font-weight: 300; color: var(--white); line-height: 1;
  }
  .footer-company { left: 48px; }
  .footer-date { left: 720px; }
  .page-code { position: absolute; left: 823px; top: 1181px; font-size: 7px; color: var(--white); }
</style>
</head>
<body>
<main class="newsletter">
  <svg class="backdrop" width="848" height="1200" viewBox="0 0 848 1200" aria-hidden="true">
    <defs>
      <linearGradient id="lower-green" x1="0" y1="0" x2="0" y2="1">
        <stop offset="0" stop-color="#7db733"/>
        <stop offset="0.55" stop-color="#5f961f"/>
        <stop offset="1" stop-color="#447510"/>
      </linearGradient>
    </defs>
    <polygon points="0,180 157,180 0,248" fill="var(--green)"/>
    <polygon points="185.5,180 457,180 282,256 13,256" fill="var(--green)"/>
    <polygon points="848,21 848,256 313.5,256" fill="var(--green)"/>
    <polygon points="0,1087 424,899 424,1200 0,1200" fill="url(#lower-green)"/>
    <rect x="0" y="1161" width="848" height="39" fill="var(--green-deep)"/>
  </svg>

  <h1 class="masthead-name">Team upBeat</h1>
  <p class="issue-date">Date</p>

  <p class="greeting">Hi everyone,</p>

  <aside class="sidebar">
    <h2 class="section-title" style="left:62px; top:69px;">Top Sellers!</h2>
    <p class="intro">The Following Restwell Team Members Were Our Top Sellers Last Week <strong>Based On Completed Sales</strong></p>
    <table class="sellers-table">
      <tr><th class="rank">#</th><th class="member">Team Member</th></tr>
      <tr><td class="rank">1</td><td class="member">- 100 Restwell Dollars</td></tr>
      <tr><td class="rank">2</td><td class="member">- 50 Restwell Dollars</td></tr>
      <tr><td class="rank">3</td><td class="member">- 25 Restwell Dollars</td></tr>
    </table>

    <h2 class="section-title" style="left:56px; top:374px;">Top Tip From Our Week’s Top Seller</h2>
    <ul class="tip-list">
      <li><svg viewBox="0 0 10 10"><circle cx="5" cy="5" r="4.2" fill="none" stroke="var(--heading-green)" stroke-width="1.2"/><path d="M3 5.1 4.4 6.4 7 3.7" fill="none" stroke="var(--heading-green)" stroke-width="1.2"/></svg>Lorem ipsum dolor sit aullamco laboris nisi utuipmnsecte turdipiscinlised doiusulboris nisi ut aliquipmod</li>
      <li><svg viewBox="0 0 10 10"><circle cx="5" cy="5" r="4.2" fill="none" stroke="var(--heading-green)" stroke-width="1.2"/><path d="M3 5.1 4.4 6.4 7 3.7" fill="none" stroke="var(--heading-green)" stroke-width="1.2"/></svg>Lorem ipsum dolor sit aullamco laboris nisi utuipmnsecte turdipiscinlised doiusulboris nisi ut aliquipmod</li>
      <li><svg viewBox="0 0 10 10"><circle cx="5" cy="5" r="4.2" fill="none" stroke="var(--heading-green)" stroke-width="1.2"/><path d="M3 5.1 4.4 6.4 7 3.7" fill="none" stroke="var(--heading-green)" stroke-width="1.2"/></svg>Lorem ipsum dolor sit aullamco laboris nisi utuipmnsecte turdipiscinlised doiusulboris nisi ut aliquipmod</li>
      <li><svg viewBox="0 0 10 10"><circle cx="5" cy="5" r="4.2" fill="none" stroke="var(--heading-green)" stroke-width="1.2"/><path d="M3 5.1 4.4 6.4 7 3.7" fill="none" stroke="var(--heading-green)" stroke-width="1.2"/></svg>Lorem ipsum dolor sit aullamco laboris nisi utuipmnsecte turdipiscinlised doiusulboris nisi ut aliquipmod</li>
    </ul>

    <h2 class="section-title" style="left:56px; top:662px;">Shout Out</h2>
    <div class="field field-name">Enter Name *</div>
    <div class="field field-comments">Comments</div>
    <div class="submit-button">SUBMIT</div>
  </aside>

  <p class="footer-text footer-company">© Restwell Loungers</p>
  <p class="footer-text footer-date">Date</p>
  <p class="page-code">C9</p>
</main>
</body>
</html>
```